EXTENDED Store hours to serve your healthcare needs

I'M LOOKING FOR A NICE FLYER THAT SHOWS THE FOLLOWING INFORMATION:

Logo
address
tel phone and fax
email address

Extending our hours to meet the growing healthcare needs of our community. Fast delivery service!

Monday - Thursday 10am-midnight
Friday 10am-4pm
Saturday - Motzei Shabbos till midnight
Sunday 10am-7pm

Target Market(s)

Community

Industry/Entity Type

Pharmacy

Requirements
Must have
• Extended hours
• personal care
• expert advice
• superior service
Nice to have
• Looking for no people pictures
• Eye popping design
• Classic modern clean design
Should not have
• store description is services
• And should not say Fiirst to open and last to close

```html
<!DOCTYPE html>
<html lang="en">
<head>
<meta charset="utf-8">
<title>Lindell Pharmacy – Extended Hours</title>
<link href="https://fonts.googleapis.com/css2?family=Open+Sans:wght@600;800&family=PT+Sans:wght@400;700&family=PT+Sans+Narrow:wght@400;700&display=swap" rel="stylesheet">
<style>
  :root{
    --day:#4bc3d6;
    --night:#044e94;
    --accent-red:#b22126;
    --band:#ededed;
    --ink:#4a4a4a;
    --ink-dark:#222;
    --label:#888;
    --brand-blue:#0d4c97;
    --white:#fff;
    --card-top:#f4f4f4;
    --card-bottom:#e2e2e2;
  }
  *{margin:0;padding:0;box-sizing:border-box}
  html,body{width:830px;height:1200px;overflow:hidden;background:var(--white)}
  .flyer{position:relative;width:830px;height:1200px;background:var(--white);font-family:"PT Sans",sans-serif}

  .hero{position:absolute;left:0;top:0;width:830px;height:612px;
    background:linear-gradient(90deg,var(--day) 0 50%,var(--night) 50% 100%)}
  .hero-scene{position:absolute;left:148px;top:305px;width:535px;height:305px;
    background:linear-gradient(180deg,#2d7bbd 0 18%,#f5f7f8 18% 88%,#bdbdbd 88% 100%)}

  .headline{position:absolute;top:140px;left:0;width:830px;text-align:center;color:var(--white);font-family:"Open Sans",sans-serif}
  .headline-kicker{display:block;font-weight:600;font-size:25px;letter-spacing:3px;line-height:30px}
  .headline-main{display:block;font-weight:800;font-size:62px;line-height:70px;letter-spacing:-1px}

  .rule{position:absolute;left:0;top:612px;width:830px;height:8px;background:var(--accent-red)}

  .tagline-band{position:absolute;left:0;top:620px;width:830px;height:120px;background:var(--band)}
  .tagline{position:absolute;left:66px;top:16px;font-size:21px;line-height:30px;letter-spacing:3.4px;color:var(--ink);font-weight:400}
  .tagline strong{font-weight:700;color:var(--accent-red)}

  .hours{position:absolute;left:45px;top:760px;width:340px;height:430px;border-left:2px solid #f0f0f0}
  .hours-card{position:absolute;left:0;width:333px;height:84px;padding:14px 0 0 20px;
    background:linear-gradient(180deg,var(--card-top),var(--card-bottom));box-shadow:0 4px 4px rgba(0,0,0,.18)}
  .hours-card:nth-child(1){top:26px}
  .hours-card:nth-child(2){top:120px}
  .hours-card:nth-child(3){top:214px}
  .hours-card:nth-child(4){top:308px}
  .hours-day{font-weight:700;font-size:19px;letter-spacing:2.5px;color:#3c3c3c;line-height:22px}
  .hours-time{font-family:"PT Sans Narrow",sans-serif;font-size:26px;color:var(--ink-dark);line-height:32px}

  .brand{position:absolute;left:432px;top:836px;font-weight:700;font-size:40px;color:var(--brand-blue);letter-spacing:1px}
  .services{position:absolute;left:432px;top:898px;font-size:16px;letter-spacing:.5px;color:var(--ink)}

  .contact{position:absolute;left:430px;top:945px;list-style:none}
  .contact li{font-size:21px;color:var(--ink-dark);height:40.6px;line-height:34px}
  .contact .key{color:var(--label);display:inline-block;width:30px}

  .social{position:absolute;left:726px;top:1082px;font-family:"Open Sans",sans-serif;font-size:15px;color:#333}
  .social-squares{display:flex;gap:4px;margin-top:4px}
  .social-squares span{width:28px;height:28px;background:var(--brand-blue);display:block}
</style>
</head>
<body>
<div class="flyer">
  <div class="hero" role="img" aria-label="Flat illustration of a pharmacy storefront between a daytime skyline with sun and clouds and a night skyline with moon and stars">
    <div class="hero-scene"></div>
  </div>
  <h1 class="headline">
    <span class="headline-kicker">EXTENDED</span>
    <span class="headline-main">STORE HOURS</span>
  </h1>
  <div class="rule"></div>

  <div class="tagline-band">
    <p class="tagline">EXTENDING OUR HOURS TO MEET THE GROWING<br>HEALTHCARE NEEDS OF OUR COMMUNITY.<br><strong>FAST DELIVERY SERVICE!</strong></p>
  </div>

  <section class="hours">
    <div class="hours-card"><p class="hours-day">MONDAY – THURSDAY</p><p class="hours-time">10am-Midnight</p></div>
    <div class="hours-card"><p class="hours-day">FRIDAY</p><p class="hours-time">10am-4pm</p></div>
    <div class="hours-card"><p class="hours-day">SATURDAY</p><p class="hours-time">Motzei Shabbos till midnight</p></div>
    <div class="hours-card"><p class="hours-day">SUNDAY</p><p class="hours-time">10am-7pm</p></div>
  </section>

  <p class="brand">Lindell Pharmacy</p>
  <p class="services">Personal care · Expert advice · Superior service</p>

  <ul class="contact">
    <li><span class="key">A:</span>48 Orchard Ave, Brooklyn, NY 11205</li>
    <li><span class="key">E:</span>hello@lindellpharmacy.com</li>
    <li><span class="key">T:</span>(718) 555-0142</li>
    <li><span class="key">F:</span>(718) 555-0187</li>
    <li><span class="key">W:</span>www.lindellpharmacy.com</li>
  </ul>

  <div class="social">
    <p>Join us:</p>
    <div class="social-squares"><span></span><span></span></div>
  </div>
</div>
</body>
</html>
```